FOLI PACK FOR STICKS

Design the packaging for salted sticks (weight 400g) reference to the logo TOVEN (in attached).
Color packaging- look forward to suggestions.
Package with window.
Hi, we need only graphic conception without texts on back side.

Please find Logo TOVEN and the grid of packaging - attached
Updates

we need only graphic conception without texts on back side. Added Saturday, November 08, 2014

Target Market(s)

typical salted snack for everyone (adults and children included)

Font styles to use
Sans Serif

Requirements
Should not have
• - religion and politic signs…
• - toys and childdraws
• - monsters, devils and demons etc.

```html
<!DOCTYPE html>
<html lang="en">
<head>
<meta charset="utf-8">
<title>TOVEN Sticks – Salted 400g Pack</title>
<link rel="stylesheet" href="https://fonts.googleapis.com/css2?family=Pacifico&family=Roboto:wght@700&display=swap">
<style>
  :root {
    --page: #ffffff;
    --trim: #c4c4c4;
    --orange-deep: #c23a06;
    --orange: #ef7a0c;
    --orange-light: #f7a53a;
    --stripe-light: #f6c79a;
    --yellow: #ffd400;
    --yellow-bright: #fff200;
    --red: #e8123c;
    --white: #ffffff;
    --brand-brown: #6b3d12;
  }
  html, body {
    margin: 0;
    width: 1200px;
    height: 846px;
    overflow: hidden;
    background: var(--page);
  }
  .pack {
    display: block;
    width: 1200px;
    height: 846px;
  }
  .brand-name {
    font-family: "Roboto", sans-serif;
    font-weight: 700;
    font-size: 22px;
    fill: var(--brand-brown);
  }
  .product-title {
    font-family: "Pacifico", cursive;
    font-size: 62px;
    fill: var(--white);
    stroke: var(--orange);
    stroke-width: 14px;
    paint-order: stroke;
    stroke-linejoin: round;
  }
  .product-title-inner {
    font-family: "Pacifico", cursive;
    font-size: 62px;
    fill: var(--yellow);
  }
  .weight {
    font-family: "Pacifico", cursive;
    font-size: 17px;
    fill: var(--white);
  }
  .flavour {
    font-family: "Pacifico", cursive;
    font-size: 42px;
    fill: var(--red);
    stroke: var(--white);
    stroke-width: 8px;
    paint-order: stroke;
    stroke-linejoin: round;
  }
</style>
</head>
<body>
<svg class="pack" viewBox="0 0 1200 846" xmlns="http://www.w3.org/2000/svg">
  <defs>
    <linearGradient id="base-glow" x1="0" y1="0" x2="0" y2="1">
      <stop offset="0" stop-color="var(--orange)"/>
      <stop offset="1" stop-color="var(--orange-deep)"/>
    </linearGradient>
    <radialGradient id="yellow-wave" cx="0.55" cy="0.35" r="0.7">
      <stop offset="0" stop-color="var(--yellow-bright)"/>
      <stop offset="0.5" stop-color="var(--yellow)"/>
      <stop offset="1" stop-color="var(--orange-deep)"/>
    </radialGradient>
    <radialGradient id="title-glow" cx="0.5" cy="0.5" r="0.5">
      <stop offset="0" stop-color="#fff6d8" stop-opacity="0.95"/>
      <stop offset="1" stop-color="#fff6d8" stop-opacity="0"/>
    </radialGradient>
    <linearGradient id="window-fill" x1="0" y1="0" x2="1" y2="1">
      <stop offset="0" stop-color="#b8621f"/>
      <stop offset="0.5" stop-color="#e0883a"/>
      <stop offset="1" stop-color="#9a4a14"/>
    </linearGradient>
    <linearGradient id="shaker-fill" x1="0" y1="0" x2="1" y2="0">
      <stop offset="0" stop-color="#f2f2f2"/>
      <stop offset="1" stop-color="#bdbdbd"/>
    </linearGradient>
    <pattern id="stripes" width="16" height="10" patternUnits="userSpaceOnUse">
      <rect width="16" height="10" fill="var(--orange)"/>
      <rect x="9" width="7" height="10" fill="var(--stripe-light)"/>
    </pattern>
    <clipPath id="pack-area">
      <rect x="221" y="183" width="810" height="499"/>
    </clipPath>
  </defs>

  <!-- trim bands -->
  <rect class="trim-right" x="1031" y="183" width="19" height="511" fill="var(--trim)"/>
  <rect class="trim-bottom" x="221" y="682" width="829" height="12" fill="var(--trim)"/>

  <g clip-path="url(#pack-area)">
    <rect x="221" y="183" width="810" height="499" fill="url(#base-glow)"/>
    <rect class="stripe-band" x="221" y="183" width="810" height="300" fill="url(#stripes)"/>
    <ellipse cx="620" cy="310" rx="170" ry="130" fill="url(#title-glow)"/>

    <!-- top-left orange swoosh -->
    <path d="M221 183 H240 C250 260 300 300 400 330 C300 330 240 320 221 310 Z" fill="var(--orange-light)"/>

    <!-- main yellow wave -->
    <path d="M221 315 C320 330 420 430 560 430 C660 430 720 350 830 355 C920 360 990 390 1031 420 V682 H221 Z" fill="url(#yellow-wave)"/>
    <!-- right light wave -->
    <path d="M700 410 C820 400 960 440 1031 560 V682 H880 C960 600 900 470 700 410 Z" fill="var(--yellow-bright)" opacity="0.55"/>
  </g>

  <!-- brand -->
  <text class="brand-name" x="622" y="238" text-anchor="middle">TOVEN</text>

  <!-- title -->
  <text class="product-title" x="620" y="340" text-anchor="middle">Sticks</text>
  <text class="product-title-inner" x="620" y="340" text-anchor="middle" opacity="0.55">Sticks</text>

  <!-- window -->
  <path class="window" role="img" aria-label="Window showing salted pretzel sticks"
        d="M620 378 C690 378 740 420 740 475 C740 520 710 548 670 555 L688 592 L640 558 C560 565 500 525 500 470 C500 418 552 378 620 378 Z"
        fill="url(#window-fill)" stroke="var(--red)" stroke-width="4"/>

  <text class="weight" x="552" y="556" transform="rotate(-22 552 556)" text-anchor="middle">400g</text>

  <!-- flavour ribbon -->
  <path class="flavour-ribbon" d="M495 585 L690 600 L712 630 L690 640 L718 672 L497 645 Z" fill="var(--yellow)"/>
  <text class="flavour" x="600" y="638" text-anchor="middle" transform="rotate(3 600 638)">salted</text>

  <!-- salt shaker -->
  <rect class="salt-shaker" role="img" aria-label="Salt shaker illustration" x="692" y="535" width="56" height="103" rx="12" fill="url(#shaker-fill)"/>
</svg>
</body>
</html>
```